School Rules Posters

I would like a design for four different posters. Each one has a different purpose:

1: The Three Main rules

2: The Rewards

3: The Consequences

4: Consequences

At the moment they are very boring and dry and I would like an icon for each rule with the text underneath?

I'd like the logo on it.

It is for a middle school so it cannot be 'too young'.

I don't mind if the posters are Portrait or Landscape. The posters need to provide pupils with clarity and cannot be too busy. They'll be made into A1.
I have attached an example from another school which has logos - I don't want the same thing but give's you an idea of icons.

```html
<!DOCTYPE html>
<html lang="en">
<head>
<meta charset="utf-8">
<title>The Hollin Way – Rules</title>
<link rel="stylesheet" href="https://fonts.googleapis.com/css2?family=Jost:wght@500;700&family=Oswald:wght@500&family=Arimo:wght@400&display=swap">
<style>
  :root {
    --purple: #94297a;
    --purple-light: #b2409a;
    --navy: #243050;
    --navy-glow: #3a5aa8;
    --orange: #fbab08;
    --orange-glow: #ffd23a;
    --teal: #63cace;
    --teal-glow: #9ff0f0;
    --white: #ffffff;
    --ink: #1f2b3a;
    --tick-green: #7cc242;
  }
  * { box-sizing: border-box; margin: 0; padding: 0; }
  html, body { width: 1200px; height: 800px; overflow: hidden; background: var(--white); }
  .poster { position: relative; width: 1200px; height: 800px; }

  .masthead {
    position: absolute; inset: 0 0 auto 0; height: 119px;
    background: linear-gradient(90deg, var(--purple-light) 0%, var(--purple) 30%, var(--purple) 100%);
    border-bottom: 2px solid var(--white);
  }
  .school-name {
    position: absolute; left: 28px; top: 20px; width: 150px;
    font-family: "Jost", sans-serif; font-weight: 700; font-size: 20px;
    line-height: 1.05; color: var(--white); text-align: center; letter-spacing: 1px;
  }
  .school-mark {
    display: block; width: 16px; height: 16px; border-radius: 50%;
    background: var(--white); margin: 0 auto 8px;
  }
  .title {
    position: absolute; left: 265px; top: 16px;
    font-family: "Jost", sans-serif; font-weight: 700; font-size: 54px;
    color: var(--white); letter-spacing: 0.5px; white-space: nowrap;
  }
  .tagline {
    position: absolute; left: 335px; top: 101px; width: 531px; height: 38px;
    background: var(--white); z-index: 2;
    font-family: "Oswald", sans-serif; font-weight: 500; font-size: 25px;
    color: var(--purple); letter-spacing: 5px; text-align: center; line-height: 38px;
  }

  .rules { position: absolute; top: 121px; left: 0; width: 1200px; height: 679px; display: flex; }
  .rule { position: relative; width: 400px; height: 100%; color: var(--white); }
  .rule--ready { background: radial-gradient(circle at 50% 110px, var(--navy-glow) 0%, var(--navy) 45%); }
  .rule--respect { background: radial-gradient(circle at 50% 110px, var(--orange-glow) 0%, var(--orange) 40%); }
  .rule--safe { background: radial-gradient(circle at 50% 110px, var(--teal-glow) 0%, var(--teal) 40%); }

  .rule__icon { position: absolute; left: 140px; top: 40px; width: 120px; height: 130px; }
  .rule__heading {
    position: absolute; top: 176px; width: 100%; text-align: center;
    font-family: "Jost", sans-serif; font-weight: 700; font-size: 41px; letter-spacing: -0.5px;
  }
  .rule__item {
    position: absolute; width: 100%; text-align: center; transform: translateY(-50%);
    font-family: "Arimo", sans-serif; font-size: 25px; line-height: 1.3;
  }
  .hands-glow {
    position: absolute; left: 160px; top: 60px; width: 80px; height: 100px; border-radius: 40px;
    background: radial-gradient(circle, #fff6b0 0%, #ffe14a 60%, rgba(255,225,74,0) 100%);
  }
</style>
</head>
<body>
<div class="poster">
  <header class="masthead">
    <div class="school-name"><span class="school-mark"></span>HOLLIN<br>MARSH</div>
    <h1 class="title">The Hollin Way – Rules</h1>
  </header>
  <div class="tagline">HELPING US BE THE BEST WE CAN BE</div>

  <main class="rules">
    <section class="rule rule--ready">
      <svg class="rule__icon" viewBox="0 0 120 130" aria-hidden="true">
        <circle cx="60" cy="14" r="8" fill="none" stroke="#fff" stroke-width="5"/>
        <rect x="55" y="20" width="10" height="12" fill="#fff"/>
        <rect x="14" y="30" width="12" height="10" rx="3" fill="#fff" transform="rotate(-40 20 35)"/>
        <circle cx="60" cy="80" r="46" fill="#fff"/>
        <circle cx="60" cy="80" r="38" fill="#2f55c4"/>
        <g stroke="#fff" stroke-width="3">
          <line x1="60" y1="46" x2="60" y2="53"/><line x1="60" y1="107" x2="60" y2="114"/>
          <line x1="26" y1="80" x2="33" y2="80"/><line x1="87" y1="80" x2="94" y2="80"/>
        </g>
        <polyline points="40,80 56,96 104,44" fill="none" stroke="var(--tick-green)" stroke-width="13" stroke-linecap="square"/>
      </svg>
      <h2 class="rule__heading">BE READY</h2>
      <p class="rule__item" style="top:277px">Punctual to meet and great</p>
      <p class="rule__item" style="top:356px">Ready to learn new ideas</p>
      <p class="rule__item" style="top:438px">Be Well-Presented</p>
      <p class="rule__item" style="top:531px">Have the right equipment</p>
      <p class="rule__item" style="top:627px">Know your &nbsp;seat</p>
    </section>

    <section class="rule rule--respect">
      <svg class="rule__icon" viewBox="0 0 120 130" aria-hidden="true" style="left:120px;width:160px;top:25px">
        <g stroke="#fff" stroke-width="5" stroke-linecap="round" transform="scale(1.333 1) translate(-15 0)">
          <line x1="60" y1="4" x2="60" y2="26"/>
          <line x1="30" y1="12" x2="40" y2="30"/><line x1="90" y1="12" x2="80" y2="30"/>
          <line x1="10" y1="40" x2="26" y2="48"/><line x1="110" y1="40" x2="94" y2="48"/>
          <line x1="2" y1="72" x2="22" y2="72"/><line x1="118" y1="72" x2="98" y2="72"/>
        </g>
      </svg>
      <div class="hands-glow" role="img" aria-label="Raised hands symbol glowing"></div>
      <h2 class="rule__heading">BE RESPECTFUL</h2>
      <p class="rule__item" style="top:277px">Raise your hand to talk</p>
      <p class="rule__item" style="top:358px">Manners give<br>a great impressions</p>
      <p class="rule__item" style="top:420px">Hold doors open for others</p>
      <p class="rule__item" style="top:504px">Respect every persons right<br>to learn and work</p>
      <p class="rule__item" style="top:600px">Show the best version of you</p>
    </section>

    <section class="rule rule--safe">
      <svg class="rule__icon" viewBox="0 0 120 130" aria-hidden="true">
        <path d="M60 8 C74 20 92 24 108 22 C108 70 92 104 60 122 C28 104 12 70 12 22 C28 24 46 20 60 8 Z" fill="#fff"/>
        <path d="M60 22 C72 31 86 35 96 34 C95 72 82 96 60 108 C38 96 25 72 24 34 C34 35 48 31 60 22 Z" fill="var(--teal)"/>
        <polyline points="40,64 56,80 100,34" fill="none" stroke="var(--ink)" stroke-width="12"/>
      </svg>
      <h2 class="rule__heading">BE SAFE</h2>
      <p class="rule__item" style="top:277px">Walk quietly around the school<br>building and grounds</p>
      <p class="rule__item" style="top:358px">Throw litter in the bin</p>
      <p class="rule__item" style="top:435px">Eat and drink in<br>the designated areas</p>
      <p class="rule__item" style="top:533px">Leave your desk tidy<br>for the next class</p>
      <p class="rule__item" style="top:626px">Look after our building<br>and grounds</p>
    </section>
  </main>
</div>
</body>
</html>
```